Buch-/E-Book-Cover für Erstveröffentlichung eines kleinen Fantasyromans
Zielgruppe
Ich habe gerade mein erstes kleineres Buch fertig geschrieben und möchte es nun über Self Publishing selbst herausbringen.
Das Buch ist eine eher niedliche kleine Geschichte über ein eher gruselig aussehendes Lebenwesen, das sich mit einem kleinen Mädchen anfreundet. Gelesen werden kann das Buch ab 12. Nach oben hin sind denke ich mal keine Grenzen.
Aufgabenstellung
Titel: Die Nebelkrähe - Ein seltsamer Sommerbund
Ich brauche ein Cover für die E-Book und Softcover Ausgabe.
Es handelt sich um ein Buch in den Maßen 12,85x19,83. Genaueres kann hier dem Anhang entnommen werden. Buchlux erstellt einem extra eine Vorlage mit allen genauen Maßen und Rändern, die eingehalten werden müssen.
Das Werk befindet sich im Moment im Lektrorat. Es kann also kleine Abweichungen zum Buchrücken geben, falls sich die Seitenzahl noch ändern sollte.
UPDATE: Das Lektorat ist nun abgeschlossen und die endgültigen Maße sind nun in der Datei enthalten.
Auf der Rückseite soll noch der Klappentext stehen. Dieser ist auch im Anhang beigefügt.
UPDATE: Die Datei wurde nochmal aktualisiert, weil noch weitere Seiten mit dabei waren, die nicht mit rein gehören.
Wer ein wenig Inspiration benötigt, kann sich auch meine Pinnwand zum Projekt auf Merkbrett ansehen.
https://www.merkbrett-beispiel.de/ErzaehlGarten/projekt-die-nebelkraehe/
Für Leute, die noch genaueren Einblick in die Atmosphäre haben wollen, gibt es die ersten Kapitel auch in der unkorrigierten Version auf meinem Blog zum lesen.
http://erzaehl-garten.blogfeld-beispiel.com/tagged/die-nebelkraehe/chrono

```html
<!DOCTYPE html>
<html lang="de">
<head>
<meta charset="utf-8">
<title>Die Nebelkrähe – Buchumschlag</title>
<link href="https://fonts.googleapis.com/css2?family=Cinzel+Decorative:wght@400;700&family=Oswald:wght@600;700&family=Open+Sans:wght@400&display=swap" rel="stylesheet">
<style>
  :root {
    --sand: #d9c4a0;
    --sand-light: #ece0c8;
    --dust: #b99f7e;
    --mist: #f5f2ee;
    --moss: #6f7a45;
    --teal: #2f6f78;
    --teal-glow: #8fe6e8;
    --shadow-figure: #3a2a2c;
    --skin: #d9a890;
    --hair: #8a5a3a;
    --title-fill: #fdf6fb;
    --title-edge: #c24fc4;
    --ink: #2b2320;
    --spine-ink: #1f1a18;
    --white: #ffffff;
  }
  * { margin: 0; padding: 0; box-sizing: border-box; }
  html, body { width: 1200px; height: 902px; overflow: hidden; background: var(--sand); }
  .cover {
    position: relative; width: 1200px; height: 902px; overflow: hidden;
    background: linear-gradient(160deg, var(--sand-light) 0%, var(--sand) 45%, var(--dust) 100%);
  }
  .art { position: absolute; }
  .art--back {
    left: 0; top: 0; width: 470px; height: 902px;
    background:
      radial-gradient(ellipse at 10% 30%, rgba(111,122,69,.75) 0%, rgba(111,122,69,0) 45%),
      radial-gradient(ellipse at 15% 70%, rgba(120,110,100,.35) 0%, rgba(120,110,100,0) 40%),
      linear-gradient(90deg, rgba(245,242,238,.9) 0%, rgba(245,242,238,.35) 60%, rgba(245,242,238,0) 100%);
  }
  .art--front {
    left: 600px; top: 0; width: 600px; height: 902px;
    background:
      radial-gradient(ellipse 120px 220px at 310px 220px, rgba(58,42,44,.85) 0%, rgba(58,42,44,0) 100%),
      radial-gradient(ellipse at 85% 75%, rgba(143,230,232,.55) 0%, rgba(47,111,120,.6) 25%, rgba(47,111,120,0) 60%),
      radial-gradient(ellipse at 90% 95%, rgba(60,90,60,.8) 0%, rgba(60,90,60,0) 45%);
  }
  .art--portrait {
    left: 600px; top: 540px; width: 265px; height: 362px;
    background: radial-gradient(ellipse at 55% 55%, var(--skin) 0%, rgba(217,168,144,.7) 35%, var(--hair) 70%, rgba(138,90,58,0) 100%);
  }
  .title {
    position: absolute; font-family: "Cinzel Decorative", serif; font-weight: 700;
    color: var(--title-fill); text-align: center; text-transform: uppercase;
    text-shadow: 0 0 2px var(--title-edge), 1px 1px 0 var(--title-edge), -1px -1px 0 var(--title-edge), 2px 3px 4px rgba(60,20,60,.55);
  }
  .title span { display: block; }
  .title--back { left: 40px; top: 18px; width: 500px; font-size: 70px; line-height: 66px; }
  .title--front { left: 640px; top: 250px; width: 520px; font-size: 86px; line-height: 75px; }
  .subtitle {
    position: absolute; left: 700px; top: 500px; width: 420px; text-align: center;
    font-family: "Oswald", sans-serif; font-weight: 700; font-size: 40px; line-height: 47px;
    color: var(--title-fill); letter-spacing: 1px; text-transform: uppercase;
    text-shadow: 1px 1px 0 var(--title-edge), -1px -1px 0 var(--title-edge), 2px 2px 4px rgba(60,20,60,.5);
  }
  .author {
    position: absolute; left: 740px; top: 16px; width: 320px; text-align: center;
    font-family: "Oswald", sans-serif; font-weight: 700; font-size: 33px; letter-spacing: 1px;
    color: var(--title-fill); text-transform: uppercase;
    text-shadow: 1px 1px 0 var(--title-edge), -1px -1px 0 var(--title-edge), 1px 2px 3px rgba(60,20,60,.5);
  }
  .spine-text {
    position: absolute; left: 599px; top: 300px; width: 300px;
    transform-origin: 0 0; transform: rotate(90deg);
    font-family: "Oswald", sans-serif; font-weight: 700; font-size: 13px; letter-spacing: .5px;
    color: var(--spine-ink); text-transform: uppercase; white-space: nowrap; text-align: center;
  }
  .blurb {
    position: absolute; left: 156px; top: 326px; width: 274px;
    font-family: "Open Sans", sans-serif; font-size: 13.3px; line-height: 19.2px;
    color: var(--ink); text-align: justify; hyphens: auto;
  }
  .barcode-area { position: absolute; left: 323px; top: 735px; width: 232px; height: 139px; background: var(--white); }
</style>
</head>
<body>
<main class="cover">
  <div class="art art--back" role="img" aria-label="Nebliger Moorwald mit Moos und dunklen Gestalten, nach links in weißen Nebel auslaufend"></div>
  <div class="art art--front" role="img" aria-label="Gemalte Schattengestalt mit roten Augen über einem Wald, Vögel am Himmel, türkis leuchtende Lichter im Moos"></div>
  <div class="art art--portrait" role="img" aria-label="Porträt eines kleinen Mädchens mit braunen Haaren und Pony"></div>

  <h2 class="title title--back"><span>Die</span><span>Nebel</span><span>Krähe</span></h2>

  <div class="blurb">
    <p>Ich wusste nicht wer ich war. Ich wusste nicht was ich war. Meine neue Gestalt war schwarz von oben bis unten. Schwarz wie ein Schatten mit stechenden roten Augen.</p>
    <p>Ich wusste nicht wie ich in diese Grotte gekommen war. Ich wusste nicht warum ich durch dieses seltsame schwarze Loch, durch das man nichts sehen konnte, nach draußen gelangen konnte. Mein neues Zuhause befand sich in einem Wald. Viele Menschen gab es in hier nicht.</p>
    <p>Was ich aber wusste, war dass ich anders war als all die normalen Menschen. Anders machte den Menschen Angst. Doch in diesem Punkt sollte ich eines besseren belehrt werden, als ich ein kleines Mädchen traf, welches mich sofort in ihr Herz schloss.</p>
  </div>

  <div class="barcode-area"></div>

  <div class="spine-text">Die Nebelkrähe &nbsp;Ein seltsamer Sommerbund</div>

  <p class="author">Lena Waldheimer</p>
  <h1 class="title title--front"><span>Die</span><span>Nebel</span><span>Krähe</span></h1>
  <p class="subtitle">Ein seltsamer<br>Sommerbund</p>
</main>
</body>
</html>
```